Corrimbel Lodge Web Design Project

I am looking for a striking, modern and user friendly site to promote my business, Corrimbel Lodge.

Corrimbel Lodge comprises of 3 elements : Restaurant, Resort and Events and the site must showcase all of these.
Updates

Project Deadline Extended
Reason: Too far away from brief ! Please check out the 2 website links to restaurant sites i LOVE for inspiration ! I am happy to pay for a quality designer and also for anyone that can code this !

Target Market(s)

Our Restaurant clientele demographic is 30-60 years old and are a mix of locals and tourists. The Restaurant is very much a destination venue so we attract people that wish to seek out amazing food.

The Event side of things attracts mainly weddings, this is a lucrative arm of the business and this side of the site must also be outstanding.

The Resort comprises of 7 boutique loft apartment and has a big pool and spa. We attract a mix of locals but want to push it as a ' getaway '

Industry/Entity Type

Business

Requirements
Must have
• I would like the first page to be an overall blog and to highlight the 3 area of the business. Lets have the 3 keywords as clickable tabs that take you to that section of the site.

RESTAURANT RESORT EVENTS

The RESTAURANT page should include the following tabs ( i have provided the information to be added to each tab as an example )

MENU ( Breakfast, Lunch, Dinner, Set Menu, Wine List)

FUNCTIONS (Private Dining Room, Exclusive Use, Wine Nights Coming Soon)

RESERVATIONS (Enquiry Form linked to my info@ address, Reservation Policies, Contact Number)

GALLERY & PRESS ( Press Articles, Latest News, What's On, Photo's, Wedding Hot Spot)

CONTACT US (Opening Times, Map, Contact Details, Sign Up For Our Newsletter, Lodgebook Link )

The RESORT page should include the following tabs :
# LOFTS & RATES
# FACILITIES
# SPECIAL OFFERS
# GALLERY
# RESERVATIONS

The EVENTS page should include the following tabs :
# WEDDINGS
# CONFERENCES
# PRIVATE EVENTS
# GALLERY
# ENQUIRY FORM
Nice to have
• Include Logo, good branding

```html
<!DOCTYPE html>
<html lang="en">
<head>
<meta charset="utf-8">
<title>Corrimbel Lodge</title>
<link rel="stylesheet" href="https://fonts.googleapis.com/css2?family=Carlito:ital,wght@0,400;0,700;1,400&family=Fredoka:wght@700&family=Raleway:wght@600&display=swap">
<style>
  :root {
    --plum: #97605f;
    --rose: #c99594;
    --rose-deep: #8f4a63;
    --white: #ffffff;
    --ink: #111111;
    --grey-text: #444444;
    --grey-soft: #8a8a8a;
    --peach: #fbe3d3;
    --sky-top: #dfe6ee;
    --sky-blue: #4a86b8;
    --lake: #5d8fb0;
    --chair-red: #d8401f;
    --deck: #8a6a55;
    --dot-line: #c8a28a;
    --dot-current: #5a3a2c;
  }
  * { margin: 0; padding: 0; box-sizing: border-box; }
  html, body { width: 1200px; height: 1000px; overflow: hidden; background: var(--white); }
  body { font-family: "Carlito", "Calibri", sans-serif; }
  .canvas { position: relative; width: 1200px; height: 1000px; overflow: hidden; }

  .panel { position: absolute; overflow: hidden; }
  .panel--brand { left: 0; top: 0; width: 395px; height: 550px; background: var(--plum); color: var(--white); }
  .panel--restaurant { left: 398px; top: 0; width: 400px; height: 550px; background: var(--rose); }
  .panel--resort { left: 800px; top: 0; width: 400px; height: 552px; background: var(--white); }
  .panel--feature { left: 0; top: 552px; width: 798px; height: 448px; }
  .panel--events { left: 798px; top: 552px; width: 402px; height: 448px; background: var(--rose); overflow: visible; }

  .brand-name { position: absolute; left: 42px; top: 52px; font-size: 60px; font-weight: 400; letter-spacing: 4px; line-height: 1; }
  .brand-sub { position: absolute; left: 42px; top: 148px; font-size: 48px; letter-spacing: 3px; line-height: 1; }
  .brand-address { position: absolute; left: 27px; top: 424px; font-size: 19px; letter-spacing: 3.5px; line-height: 31px; font-style: normal; }
  .brand-email { position: absolute; left: 27px; top: 523px; font-size: 15px; font-style: italic; letter-spacing: 0.6px; }
  .brand-social { position: absolute; right: 24px; top: 522px; font-size: 15px; letter-spacing: 1px; }

  .section-title { position: absolute; left: 17px; top: 150px; font-size: 46px; letter-spacing: 11px; color: var(--ink); font-weight: 400; line-height: 1; white-space: nowrap; }
  .restaurant-nav { position: absolute; left: 17px; top: 220px; list-style: none; }
  .restaurant-nav li { font-size: 42px; letter-spacing: 8.5px; color: var(--white); line-height: 70px; white-space: nowrap; }
  .restaurant-nav .is-active { color: var(--rose-deep); }

  .resort-word { position: absolute; left: 42px; top: 0; width: 250px; height: 545px; }
  .resort-letter {
    position: absolute; font-family: "Fredoka", sans-serif; font-weight: 700; font-size: 190px; line-height: 1;
    background: linear-gradient(180deg, var(--sky-top) 0%, var(--sky-blue) 30%, var(--lake) 48%, var(--chair-red) 65%, var(--deck) 85%, var(--chair-red) 100%);
    background-size: 100% 545px;
    -webkit-background-clip: text; background-clip: text; color: transparent;
  }
  .resort-letter--r1 { left: 0; top: -12px; background-position: 0 12px; }
  .resort-letter--e  { left: 145px; top: -12px; background-position: 0 12px; }
  .resort-letter--s  { left: 0; top: 175px; background-position: 0 -175px; }
  .resort-letter--o  { left: 135px; top: 175px; background-position: 0 -175px; }
  .resort-letter--r2 { left: 0; top: 360px; background-position: 0 -360px; }
  .resort-letter--t  { left: 145px; top: 360px; background-position: 0 -360px; }

  .resort-nav { position: absolute; left: 303px; top: 436px; list-style: none; }
  .resort-nav li { font-size: 14px; color: var(--grey-text); line-height: 24px; }
  .resort-nav .is-muted { color: var(--grey-soft); }
  .resort-cta { position: absolute; right: 6px; top: 536px; font-size: 13px; color: var(--grey-soft); letter-spacing: 0.5px; white-space: nowrap; }

  .feature-photo { position: absolute; inset: 0; background: radial-gradient(ellipse at 50% 70%, #5a3a2c 0%, #3c2a22 38%, #a98467 60%, #f4e6da 85%, #fbf1e8 100%); }
  .carousel-dot { position: absolute; top: 427px; width: 10px; height: 10px; border: 1.5px solid var(--dot-line); transform: rotate(45deg); }
  .carousel-dot.is-current { border-color: var(--dot-current); }

  .events-rose { position: absolute; left: -12px; width: 46px; height: 46px; border-radius: 50%; background: radial-gradient(circle, #fff6e4 0%, #f1ebdf 60%, #d9d4c6 100%); }
  .events-title { position: absolute; left: 26px; top: 150px; font-family: "Raleway", sans-serif; font-weight: 600; font-size: 72px; letter-spacing: 10px; color: var(--peach); line-height: 1; white-space: nowrap; }
  .events-nav { position: absolute; left: 42px; top: 290px; width: 340px; list-style: none; display: flex; flex-wrap: wrap; column-gap: 70px; row-gap: 0; }
  .events-nav li { font-size: 19px; font-style: italic; letter-spacing: 4px; color: var(--white); line-height: 38px; height: 38px; white-space: nowrap; }
</style>
</head>
<body>
<main class="canvas">

  <header class="panel panel--brand">
    <h1 class="brand-name">Corrimbel</h1>
    <p class="brand-sub">Lodge</p>
    <address class="brand-address">14 Ridgeline Road<br>Bellmount NSW 2290</address>
    <p class="brand-email">stay@corrimbellodge.com.au</p>
    <p class="brand-social">Lodgebook</p>
  </header>

  <section class="panel panel--restaurant">
    <h2 class="section-title">RESTAURANT</h2>
    <ul class="restaurant-nav">
      <li>Menu</li>
      <li>Functions</li>
      <li class="is-active">Reservation</li>
      <li>Gallery&amp;Press</li>
    </ul>
  </section>

  <section class="panel panel--resort">
    <h2 class="resort-word" role="img" aria-label="RESORT lettering filled with a photo of sky, lake and red deck chairs">
      <span class="resort-letter resort-letter--r1">R</span>
      <span class="resort-letter resort-letter--e">E</span>
      <span class="resort-letter resort-letter--s">S</span>
      <span class="resort-letter resort-letter--o">O</span>
      <span class="resort-letter resort-letter--r2">R</span>
      <span class="resort-letter resort-letter--t">T</span>
    </h2>
    <ul class="resort-nav">
      <li>Loft &amp; rates</li>
      <li>Facilities</li>
      <li>Special Offers</li>
      <li class="is-muted">Gallery</li>
    </ul>
    <p class="resort-cta">&#9671; RESERVATIONS &#9671;</p>
  </section>

  <section class="panel panel--feature">
    <div class="feature-photo" role="img" aria-label="Close-up photo of a glazed chocolate dessert beside cream"></div>
    <span class="carousel-dot is-current" style="left:674px"></span>
    <span class="carousel-dot" style="left:703px"></span>
    <span class="carousel-dot" style="left:731px"></span>
    <span class="carousel-dot" style="left:761px"></span>
  </section>

  <section class="panel panel--events">
    <div class="events-rose" style="top:16px" role="img" aria-label="White rose"></div>
    <div class="events-rose" style="top:110px" role="img" aria-label="White rose"></div>
    <div class="events-rose" style="top:245px" role="img" aria-label="White rose"></div>
    <div class="events-rose" style="top:410px;left:10px" role="img" aria-label="Pale pink rose"></div>
    <h2 class="events-title">EVENTS</h2>
    <ul class="events-nav">
      <li>weddings</li>
      <li>conferences</li>
      <li>private events</li>
    </ul>
  </section>

</main>
</body>
</html>
```